Modern, upmarket label design for food product

We need a label design for a food company producing nuts with sesame and honey. In fact, we would like the words "Cashews med sesam & honning" on the label (It's in Danish and means - Cashews with sesame & honey). It should be easy for the customer to quickly understand what it is.

It is a shelf product in the competitive food industry, which is why the design should wake the feeling of 'just wanting to grab the product down from the shelves'. So, the design should stand out and have an image of a cool, modern, hip product. This being said, I love a raw & handmade look.

The company is called Tyvo. Its origins are from the danish word Pilt that is a Danish slang for yummy. I have uploaded a photo of the package the products will be sold in.

Info & dimensions on bag in picture 1.
Dimensions: 6" x 9" | 15.2 cm x 22.3 cm
Capacity: 8 ounces | 250 grams (based on whole bean coffee)

Picture 2 is the same product, but has the possibility of attaching to a hanger on shelfs.

Picture 3 - I have also uploaded a photo of a product bag, where the hole is linear instead of a round hole. The designer chooses, which bag they will like to work with!

Please let me know if there are any questions!

Target Market(s)

Target market could really be any age, but the design needs to compel the target audience to pick it from the shelves. The package should signal a product you want to hold and have other people seeing you have it. The target audience is people who cares for what they buy, and typically doesn't want a low-end or budget product. They want the whole thing, meaning it has to taste good, look good etc. They are also the type of people who like to show off whatever products they buy by placing them in their houses for their guests to see. Or by uploading pictures of it on social medias.

Industry/Entity Type

It Company

Font styles to use
Other font styles liked:
• Not a must, but I like the 'Panton' script

Requirements
Must have
• My project must have the words 'Cashews med sesam & honning' on the label, so the customer will know within a second what they are looking at and buying.
Nice to have
• I am picturing the label with the words 'Cashews med sesam & honning' as a statement, again, emphasizing how the customer instantly should know what the product is. This being said, it should not be the only thing on the package and I love a raw & handmade look - which inspiration picture 5 is a great example of!
• I have uploaded photos of what I think looks good. With this said, I am not looking for a copy of those products, but see them as good inspiration. I have named the photos inspiration 1, 2, 3, 4 & 5.
• If needed, more text can be put on the label. For example 'vegan', 'laktosefri', Glutenfri', or 'Sund Snack' are great words for being used on the label.
Should not have
• The fonts on the label should not be too decorative. Personally I like an easy too read font.

```html
<!DOCTYPE html>
<html lang="da">
<head>
<meta charset="utf-8">
<title>Tyvo – Cashews med sesam &amp; honnig</title>
<link rel="stylesheet" href="https://fonts.googleapis.com/css2?family=Barlow+Condensed:wght@600&family=Barlow:wght@600;700&display=swap">
<style>
  :root {
    --page: #ffffff;
    --kraft: #9c8a6e;
    --gold: #d4a800;
    --ink: #4a3510;
    --window: #000000;
    --nut-tone: #8c7c63;
  }
  html, body {
    margin: 0;
    width: 1200px;
    height: 897px;
    overflow: hidden;
    background: var(--page);
  }
  .label {
    position: absolute;
    left: 352px;
    top: 86px;
    width: 495px;
    height: 724px;
    background: var(--kraft);
    overflow: hidden;
  }
  .hang-hole {
    position: absolute;
    left: 233px;
    top: 34px;
    width: 30px;
    height: 30px;
    border-radius: 50%;
    background: var(--window);
  }
  .nut-art {
    position: absolute;
    background: var(--nut-tone);
    border-radius: 50%;
    opacity: 0.8;
  }
  .brand {
    position: absolute;
    left: 0;
    right: 0;
    top: 156px;
    margin: 0;
    text-align: center;
    font-family: "Barlow", sans-serif;
    font-weight: 700;
    font-size: 38px;
    letter-spacing: 2px;
    line-height: 1;
    color: var(--gold);
  }
  .tagline-band {
    position: absolute;
    left: 0;
    right: 0;
    top: 202px;
    height: 27px;
    background: var(--gold);
    display: flex;
    align-items: center;
    justify-content: center;
    font-family: "Barlow", sans-serif;
    font-weight: 600;
    font-size: 13px;
    letter-spacing: 2.5px;
    color: var(--ink);
  }
  .product-name {
    position: absolute;
    left: 0;
    right: 0;
    top: 236px;
    margin: 0;
    text-align: center;
    font-family: "Barlow Condensed", sans-serif;
    font-weight: 600;
    font-size: 62px;
    line-height: 54px;
    color: var(--ink);
    text-transform: uppercase;
  }
  .window {
    position: absolute;
    left: 131px;
    top: 374px;
    width: 234px;
    height: 234px;
    border-radius: 50%;
    background: var(--window);
  }
  .weight-band {
    position: absolute;
    left: 0;
    right: 0;
    bottom: 0;
    height: 46px;
    background: var(--gold);
    display: flex;
    align-items: center;
    justify-content: center;
    font-family: "Barlow Condensed", sans-serif;
    font-weight: 600;
    font-size: 26px;
    color: var(--ink);
  }
</style>
</head>
<body>
  <div class="label">
    <div class="hang-hole"></div>

    <div class="nut-art" role="img" aria-label="Pencil sketch of a cashew nut" style="left:37px;top:105px;width:111px;height:89px;transform:rotate(-20deg)"></div>
    <div class="nut-art" role="img" aria-label="Pencil sketch of a cashew nut" style="left:354px;top:112px;width:118px;height:75px;transform:rotate(10deg)"></div>
    <div class="nut-art" role="img" aria-label="Pencil sketch of a cashew nut" style="left:31px;top:368px;width:71px;height:112px;transform:rotate(-10deg)"></div>
    <div class="nut-art" role="img" aria-label="Pencil sketch of a cashew nut" style="left:371px;top:378px;width:106px;height:81px;transform:rotate(15deg)"></div>
    <div class="nut-art" role="img" aria-label="Pencil sketch of a cashew nut" style="left:34px;top:548px;width:102px;height:89px;transform:rotate(20deg)"></div>
    <div class="nut-art" role="img" aria-label="Pencil sketch of a cashew nut" style="left:378px;top:534px;width:75px;height:110px;transform:rotate(-15deg)"></div>

    <p class="brand">TYVO</p>
    <div class="tagline-band">SUNDE SNACKS</div>
    <h1 class="product-name">Cashews med<br>sesam &amp; honnig</h1>
    <div class="window"></div>
    <div class="weight-band">250 G</div>
  </div>
</body>
</html>
```